International Travel Technology R&D business needs a wordpress website

We are a start up team of initially 2 individuals but plan to grow our team quickly, we have deep experience in travel technology. Our goal is to provide next generation technology research and development on behalf of our clients who are leading players in the travel technology industry. Attached our logos.

Target Market(s)

Travel Technology companies

Industry/Entity Type

Travel Industry

Coding

Coded - Design and coding required

Font styles to use
Sans Serif

Requirements
Must have
• Make use of our logo and colour scheme in the attached. Has to have a sense of adventure/ stepping into the unknown but equally must convey a sense of professionalism , we are a safe pair of hands. Sample themes are in the attachment .
Nice to have
• We have identified a theme on layoutgrove which we feel would be inspirational. We hahe attached them to help in the design as inspiration.
Should not have
• images of airplanes , hotels etc, we want to project a future image.

```html
<!DOCTYPE html>
<html lang="en">
<head>
<meta charset="utf-8">
<title>Nova Transit Labs</title>
<link href="https://fonts.googleapis.com/css2?family=Orbitron:wght@700;800&family=Open+Sans:wght@400;600;700&display=swap" rel="stylesheet">
<style>
:root{
  --purple:#2d2a6b;
  --purple-light:#3d3a85;
  --blue:#29a3dd;
  --green:#3fb54b;
  --ink:#333340;
  --grey:#6b6b78;
  --card:#ececf2;
  --footer:#121214;
  --white:#ffffff;
}
*{box-sizing:border-box;margin:0;padding:0}
html,body{width:1200px;height:4749px;overflow:hidden}
body{position:relative;background:var(--white);font-family:"Open Sans",Arial,sans-serif;color:var(--ink);font-size:13px;line-height:1.6}
.abs{position:absolute}
.heading{font-family:"Orbitron","Arial Black",sans-serif;font-weight:800;letter-spacing:1px;text-transform:uppercase}
.spine{position:absolute;left:599px;top:780px;height:2780px;border-left:2px dashed #c9c9d4;z-index:0}
section,header,nav,footer{position:absolute;left:0;width:1200px}
.btn{display:inline-block;border-radius:16px;font-size:11px;font-weight:700;text-transform:uppercase;text-align:center;letter-spacing:.5px}
.btn-outline{border:2px solid var(--green);color:var(--green);background:var(--white);width:140px;height:30px;line-height:26px}
.btn-solid{background:var(--green);color:var(--white);width:150px;height:36px;line-height:36px;border-radius:18px}
.mark{width:46px;height:46px;border-radius:50%;background:var(--green);position:absolute;left:577px}

/* header */
.site-header{top:0;height:105px;background:var(--white)}
.brand{position:absolute;left:0;width:1200px;top:26px;text-align:center}
.brand-dot{display:inline-block;width:22px;height:22px;border-radius:50%;background:var(--purple);vertical-align:middle;margin-right:8px}
.brand-name{font-family:"Open Sans",sans-serif;font-weight:700;font-size:22px;color:var(--purple);vertical-align:middle;letter-spacing:1px}
.top-contact{position:absolute;right:150px;top:36px;text-align:right;font-size:12px;font-weight:600;color:var(--purple);line-height:1.5}
.phone-badge{position:absolute;right:118px;top:40px;width:28px;height:28px;border-radius:50%;border:2px solid var(--green)}

/* nav */
.main-nav{top:105px;height:45px;background:var(--purple);display:flex;justify-content:center}
.main-nav a{color:var(--white);text-decoration:none;font-size:12px;font-weight:600;padding:0 20px;line-height:45px}
.main-nav a.active{background:var(--purple-light);color:#8fd2f2}

/* hero */
.hero{top:150px;height:628px;background:radial-gradient(ellipse 900px 260px at 50% 470px,#3b7ed6 0%,#1a3f8e 35%,#0b1636 70%,#050914 100%);clip-path:polygon(0 0,100% 0,100% 84%,50% 100%,0 84%)}
.hero h1{position:absolute;top:140px;width:100%;text-align:center;color:var(--white);font-size:38px}
.hero p{position:absolute;top:195px;width:100%;text-align:center;color:var(--white);font-size:22px;font-weight:700}
.hero .btn-solid{position:absolute;top:248px;left:515px;width:170px}

/* who */
.who{top:778px;height:425px}
.section-title{position:absolute;width:100%;text-align:center;color:var(--purple);font-size:38px}
.who .text{position:absolute;left:160px;width:880px;top:147px;color:var(--grey);text-align:justify;font-size:13px}
.who .btn-outline{position:absolute;left:530px;top:277px}

/* services */
.services{top:1203px;height:595px;background:linear-gradient(120deg,#0a1a48 0%,#143a7a 40%,#1e6fb2 70%,#0b1c4a 100%)}
.side-blue{position:absolute;left:0;top:0;width:380px;height:100%;background:var(--blue)}
.side-title{position:absolute;left:143px;color:var(--white);font-size:34px;line-height:1.15}
.side-text{position:absolute;left:143px;width:225px;color:var(--white);font-size:12px;line-height:1.55}
.service-card{position:absolute;left:380px;top:79px;width:680px;height:364px;background:var(--white);padding:22px 24px}
.service{display:flex;gap:20px;margin-bottom:18px}
.service .ico{flex:none;width:72px;height:72px;border-radius:50%;border:3px solid var(--purple);display:flex;align-items:center;justify-content:center}
.service h3{color:var(--green);font-size:15px;font-weight:700;text-transform:uppercase;line-height:1.3}
.service p{font-size:12px;color:var(--ink);line-height:1.5}

/* project */
.project{top:1798px;height:582px}
.project-photo{position:absolute;left:143px;top:165px;width:442px;height:285px;background:linear-gradient(160deg,#cfe6ef 0%,#a7c98a 55%,#6b8f3e 100%)}
.project-info{position:absolute;left:612px;top:158px;width:360px}
.project-info h2{font-size:21px;font-weight:700;color:var(--ink);line-height:1.3}
.project-info p{font-size:12px;color:var(--grey);margin-top:6px;line-height:1.5}
.skill{margin-top:14px;font-size:11px;font-weight:700;text-transform:uppercase;color:var(--ink)}
.skill .row{display:flex;justify-content:space-between;width:350px}
.bar{height:7px;background:#e1e1e8;width:350px;margin-top:3px}
.bar span{display:block;height:100%;background:var(--blue)}
.project-info .btn-outline{margin-top:20px}

/* clients */
.clients{top:2380px;height:517px;background:radial-gradient(ellipse at 70% 40%,#2d3f73 0%,#151b3a 45%,#07091a 100%)}
.client-logo{position:absolute;left:380px;width:125px;height:120px;background:var(--white);display:flex;align-items:center;justify-content:center;gap:6px}
.client-logo .sq{width:14px;height:14px;background:var(--blue)}
.client-logo span{font-weight:700;font-size:16px;color:var(--purple)}
.quote{position:absolute;left:505px;width:555px;background:var(--card);padding:14px 22px 12px 52px;font-size:12px;color:var(--ink);font-style:italic;line-height:1.5}
.quote::before{content:"\201C";position:absolute;left:18px;top:2px;font-size:46px;color:var(--blue);font-style:normal;font-weight:700}
.quote b{display:block;font-style:normal;font-size:11px;margin-top:6px}

/* news */
.news{top:2897px;height:665px}
.news-card{position:absolute;top:243px;width:285px;text-align:center}
.news-photo{height:185px;position:relative}
.date{position:absolute;right:0;top:0;width:44px;height:46px;background:var(--purple);color:var(--white);font-weight:700;font-size:17px;line-height:1.1;padding-top:6px}
.date small{display:block;font-size:9px}
.news-card h3{color:var(--blue);font-size:14px;font-weight:700;margin-top:14px;line-height:1.35}
.news-card p{font-size:12px;color:var(--grey);margin-top:8px;line-height:1.5}
.news-card .btn-outline{margin-top:14px}

/* contact */
.contact{top:3562px;height:838px}
.contact-photo{position:absolute;top:143px;left:0;width:1200px;height:695px;background:linear-gradient(180deg,#f6b88a 0%,#e88b6a 25%,#a85a63 50%,#4a2b4a 75%,#1c1226 100%)}
.contact-panel{position:absolute;left:0;top:190px;width:434px;height:285px;background:var(--purple);padding:26px 0 0 143px;color:var(--white)}
.contact-panel h2{font-size:32px;line-height:1.15}
.contact-panel ul{list-style:none;margin-top:22px;font-size:12px;font-weight:600;line-height:1.7}
.socials{display:flex;gap:8px;margin-top:14px}
.socials i{width:28px;height:28px;border-radius:50%;border:2px solid var(--white);display:block}
.contact-form{position:absolute;left:377px;top:250px;width:680px;height:228px;background:var(--white);padding:18px 16px;display:flex;gap:14px}
.fields{width:325px;display:flex;flex-direction:column;gap:8px}
.field{height:36px;background:#f1f1f5;border:1px solid #dcdce4;font-size:11px;color:var(--grey);padding:8px 10px}
.field.msg{flex:1;height:118px}
.contact-form .btn-solid{position:absolute;left:318px;top:178px;width:120px;height:32px;line-height:32px}
.back-band{position:absolute;left:0;top:738px;width:1200px;height:62px;background:rgba(10,8,20,.55);color:var(--white);text-align:center;line-height:62px;font-size:13px;font-weight:600}

/* footer */
.site-footer{top:4400px;height:349px;background:var(--footer);color:#c8c8d0}
.col{position:absolute;top:92px;width:215px}
.col h4{font-family:"Orbitron",sans-serif;color:var(--blue);font-size:14px;text-transform:uppercase;margin-bottom:10px;letter-spacing:1px}
.col ul{list-style:none;font-size:11px;line-height:1.85}
.thumbs{display:grid;grid-template-columns:repeat(3,64px);gap:6px}
.thumbs i{height:44px;display:block}
.news-item{display:flex;gap:8px;font-size:10px;line-height:1.35;margin-bottom:9px}
.news-item i{flex:none;width:30px;height:30px;background:#4a6aa0;display:block}
.footer-socials i{border-color:#c8c8d0;width:24px;height:24px}
.site-footer .btn-solid{width:110px;height:28px;line-height:28px;margin-top:12px}
.copyright{position:absolute;top:318px;width:100%;text-align:center;font-size:10px;color:#7a7a86}
</style>
</head>
<body>

<div class="spine"></div>

<header class="site-header">
  <div class="brand"><span class="brand-dot"></span><span class="brand-name">NOVA TRANSIT LABS</span></div>
  <div class="top-contact">555.010.2040<br>info@novatransitlabs.com</div>
  <div class="phone-badge"></div>
</header>

<nav class="main-nav">
  <a class="active">HOME</a><a>ABOUT US</a><a>SERVICES</a><a>PROJECTS</a><a>NEWS</a><a>CONTACT US</a>
</nav>

<section class="hero" role="img" aria-label="Earth seen from space with a glowing horizon">
  <h1 class="heading">Your Message Goes Here</h1>
  <p>Lorem ipsum dolor sit amet consectetur</p>
  <span class="btn btn-solid">Get in touch »</span>
</section>

<section class="who">
  <div class="mark" style="top:40px"></div>
  <h2 class="section-title heading" style="top:78px">Who We Are</h2>
  <p class="text">Lorem ipsum dolor sit amet, consectetur adipiscing elit. Aliquam euismod eu justo nec lobortis. Maecenas eget odio facilisis, pellentesque tellus vel, luctus augue. Sed ullamcorper, ante et molestie laoreet, libero mi hendrerit est, sed tempus lacus velit quis dolor. Nullam laoreet aliquam dolor at sollicitudin. Integer eu sodales magna, vel semper turpis. Aliquam suscipit purus ante, in auctor nibh ullamcorper at. Suspendisse pellentesque rutrum metus, nec lobortis eros placerat vitae. Proin purus lorem, viverra quis nulla in, pulvinar facilisis metus. Vestibulum ante ipsum primis in faucibus orci luctus et ultrices posuere cubilia curae. Duis at enim sed sapien ultricies laoreet eu at enim. Maecenas pharetra at mauris at efficitur pellentesque habitant morbi.</p>
  <span class="btn btn-outline">Read more »</span>
</section>

<section class="services" role="img" aria-label="Blue digital background with rows of binary code">
  <div class="side-blue"></div>
  <h2 class="side-title heading" style="top:130px">Our<br>Services</h2>
  <p class="side-text" style="top:232px">Proin venenatis ultricies ipsum a commodo. Nullam id enim in velit iaculis imperdiet id nec lacus. Etiam nibh tellus, sodales id consectetur sed, egestas ac lacus. Nam id mi id felis laoreet mollis. Aliquam sodales volutpat consequat neque habitant morbi tristique.</p>
  <div class="service-card">
    <div class="service">
      <div class="ico"><svg width="38" height="38" viewBox="0 0 38 38" fill="none" stroke="#2d2a6b" stroke-width="3"><circle cx="19" cy="19" r="8"/><path d="M19 3v6M19 29v6M3 19h6M29 19h6M8 8l4 4M26 26l4 4M8 30l4-4M26 12l4-4"/></svg></div>
      <div><h3>Research</h3><p>Nam at enim accumsan, pulvinar ligula in, luctus dui. Suspendisse placerat nulla nec ex luctus fringilla. Curabitur hendrerit nulla lectus, volutpat efficitur eros rhoncus ac. Ut dictum ut purus eu lacinia. Curabitur pellentesque erat ut lorem auctor, quis finibus lacus blandit.</p></div>
    </div>
    <div class="service">
      <div class="ico"><svg width="38" height="38" viewBox="0 0 38 38" fill="none" stroke="#2d2a6b" stroke-width="3"><path d="M6 32h26M10 32V20M19 32V10M28 32V15"/></svg></div>
      <div><h3>Development</h3><p>In vestibulum, elit sit amet aliquam ornare, erat lacus tincidunt massa, a laoreet diam est nec eros. Vivamus porttitor pellentesque libero, sit amet facilisis est accumsan feugiat. Sed blandit est orci, non consectetur orci ultrices at. Duis vulputate accumsan libero pellentesque.</p></div>
    </div>
    <div class="service">
      <div class="ico"><svg width="40" height="36" viewBox="0 0 40 36" fill="none" stroke="#2d2a6b" stroke-width="3"><path d="M4 4h20v13H12l-6 5v-5H4z"/><path d="M28 12h8v13h-2v5l-6-5H16v-4"/></svg></div>
      <div><h3>Consulting</h3><p>Fusce tortor nisl, malesuada eu turpis pulvinar, congue volutpat arcu. Nullam felis enim, bibendum eu justo vel, vulputate laoreet lacus. Nunc leo nisi, tempus varius pellentesque ut, semper in velit. Maecenas pellentesque ante ac dui accumsan gravida. Sed sit amet dapibus dui.</p></div>
    </div>
  </div>
</section>

<section class="project">
  <div class="mark" style="top:60px"></div>
  <h2 class="section-title heading" style="top:100px">Latest Project</h2>
  <div class="project-photo" role="img" aria-label="Child in a space helmet holding a toy rocket outdoors"></div>
  <div class="project-info">
    <h2>Project Title Goes Here</h2>
    <p>Curabitur bibendum nulla lectus, volutpat efficitur eros rhoncus ac. Ut dictum ut purus eu lacinia. Curabitur pellentesque erat ut lorem auctor, quis finibus lacus blandit aenean eu est, lacinia ut sodales ut dapibus eu est. Phasellus dapibus sapien vitae dui ornare, in vehicula massa imperdiet. Nam efficitur lacus lectus, a hendrerit dolor iaculis enim porta sed sem dapibus.</p>
    <div class="skill"><div class="row"><span>Research</span><span>90%</span></div><div class="bar"><span style="width:90%"></span></div></div>
    <div class="skill"><div class="row"><span>Design</span><span>85%</span></div><div class="bar"><span style="width:85%"></span></div></div>
    <div class="skill"><div class="row"><span>Development</span><span>55%</span></div><div class="bar"><span style="width:55%"></span></div></div>
    <span class="btn btn-outline">Details »</span>
  </div>
</section>

<section class="clients" role="img" aria-label="Deep space nebula with distant stars">
  <div class="side-blue"></div>
  <h2 class="side-title heading" style="top:135px">Happy<br>Clients</h2>
  <p class="side-text" style="top:222px">Sed efficitur urna vel eleifend pellentesque. Duis id iaculis lectus. Class aptent taciti sociosqu ad litora torquent per conubia nostra, per inceptos himenaeos quisque semper, purus non pellentesque.</p>
  <div class="client-logo" style="top:90px"><i class="sq"></i><span>Stayfinder</span></div>
  <div class="quote" style="top:100px">Morbi cursus massa sit amet pulvinar sed efficitur urna vel eleifend pellentesque duis id iaculis lectus. Class aptent taciti sociosqu ad litora torquent per conubia nostra, per inceptos himenaeos quisque semper purus nec pellentesque.<b>Helena Voss / Stayfinder B.V. / Rotterdam</b></div>
  <div class="client-logo" style="top:270px"><i class="sq"></i><span>Roomnest</span></div>
  <div class="quote" style="top:280px">Aliquam nec dui vel lectus eleifend maximus. Sed eu turpis tempus tellus volutpat suscipit vel non nulla. Donec molestie mauris et turpis ullamcorper, ac porta tortor pulvinar. Sed vel arcu dignissim, efficitur ligula eget vehicula arcu pellentesque.<b>Daniel Marsh / Roomnest, Inc. / Portland</b></div>
</section>

<section class="news">
  <div class="mark" style="top:138px"></div>
  <h2 class="section-title heading" style="top:170px">Recent News</h2>
  <article class="news-card" style="left:143px">
    <div class="news-photo" role="img" aria-label="Rocket on the launch pad at dusk" style="background:linear-gradient(180deg,#7a5fb0,#d88a7a 60%,#3a2e5a)"><div class="date">30<small>MAY</small></div></div>
    <h3>Aliquam euismod eu justo nec lobortismaecenas eget odio facilisis</h3>
    <p>Nullam laoreet aliquam dolor at sollicitudin. Integer eu sodales magna, vel semper turpis. Aliquam suscipit purus ante, in auctor nibh ullamcorper at. Suspendisse pellentesque rutrum metus, nec lobortis eros placerat vitae.</p>
    <span class="btn btn-outline">Read more »</span>
  </article>
  <article class="news-card" style="left:459px">
    <div class="news-photo" role="img" aria-label="Traveller walking through a glowing futuristic tunnel" style="background:linear-gradient(180deg,#2a6fb0,#6ec3e6 50%,#e07aa0)"><div class="date">25<small>MAY</small></div></div>
    <h3>Sed ullamcorper ante et molestie laoreet libero mi hendrerit est</h3>
    <p>Maecenas eget odio facilisis, pellentesque tellus vel, luctus augue. Sed ullamcorper, ante et molestie laoreet, libero mi hendrerit est, sed tempus lacus velit quis dolor. Nullam laoreet aliquam dolor at sollicitudin.</p>
    <span class="btn btn-outline">Read more »</span>
  </article>
  <article class="news-card" style="left:769px">
    <div class="news-photo" role="img" aria-label="Small round robot on a desert plain" style="background:linear-gradient(180deg,#e6ddd0,#d8b58a 60%,#a8865a)"><div class="date">18<small>MAY</small></div></div>
    <h3>Nullam felis enim interdum justo vel vulputate laoreet lacus</h3>
    <p>Vestibulum a nunc magna. Vivamus venenatis vulputate tortor eu imperdiet. Nam sed nunc et purus rhoncus scelerisque a nec augue. Etiam a purus diam. Ut pellentesque, orci a tempor convallis, massa magna mattis nunc.</p>
    <span class="btn btn-outline">Read more »</span>
  </article>
</section>

<section class="contact">
  <div class="mark" style="top:10px;width:90px;height:90px;left:555px"></div>
  <div class="contact-photo" role="img" aria-label="Lone explorer standing among mountains under a sunset sky"></div>
  <div class="contact-panel">
    <h2 class="heading">Get<br>In Touch</h2>
    <ul><li>☏ 555.010.2040</li><li>✉ info@novatransitlabs.com</li><li>⌖ Austin, TX</li></ul>
    <div class="socials"><i></i><i></i><i></i></div>
  </div>
  <form class="contact-form">
    <div class="fields"><div class="field">Name</div><div class="field">Email</div><div class="field">Phone</div></div>
    <div class="fields"><div class="field msg">Message</div></div>
    <span class="btn btn-solid">Submit »</span>
  </form>
  <div class="back-band">Go Back To Space »</div>
</section>

<footer class="site-footer">
  <div class="col" style="left:143px"><h4>Sitemap</h4>
    <ul><li>› Home</li><li>› About Us</li><li>› Services</li><li>› Projects</li><li>› News</li><li>› Contact Us</li><li>› Testimonials</li></ul></div>
  <div class="col" style="left:378px"><h4>Projects</h4>
    <div class="thumbs" role="img" aria-label="Grid of project thumbnail photos">
      <i style="background:#3b5f9a"></i><i style="background:#c48a6a"></i><i style="background:#5a8ac0"></i>
      <i style="background:#7a6aa0"></i><i style="background:#4a7a5a"></i><i style="background:#b0a080"></i>
      <i style="background:#2a4a7a"></i><i style="background:#d0906a"></i><i style="background:#6a8ab0"></i>
    </div></div>
  <div class="col" style="left:612px"><h4>Recent News</h4>
    <div class="news-item"><i></i><span>Aliquam euismod eu justo nec lobortismaecenas odio facilisis</span></div>
    <div class="news-item"><i></i><span>Sed ullamcorper ante et molestie laoreet libero mi hendrerit</span></div>
    <div class="news-item"><i></i><span>Nullam felis enim interdum justo vel vulputate laoreet</span></div>
    <div class="news-item"><i></i><span>Nunc consectetur facilisis ultrices sed tincidunt lobortis finibus</span></div></div>
  <div class="col" style="left:846px"><h4>Contact Us</h4>
    <ul><li>☏ 555.010.2040</li><li>✉ info@novatransitlabs.com</li><li>⌖ Austin, TX</li></ul>
    <div class="socials footer-socials"><i></i><i></i><i></i></div>
    <span class="btn btn-solid">Hire Form »</span></div>
  <div class="copyright">©2024 Nova Transit Labs | Terms &amp; Conditions</div>
</footer>

</body>
</html>
```